Cobaltine Pilates Summer Promotions

I would like to create 2 x A6 one-side flyers for my Cobaltine Pilates private yoga summer promotions. I have 2 promotions available (bring a friend for free + 4 for price of 3 package). I would like the 2 flyers to look similar in style but would like them to look different enough so they catch the eye of the customer that there are 2 different promotions available.
Attached is my PowerPoint "versions" which I created myself but would like them to be taken to the next level for professionalism and design. You do not have to follow this layout - this was just my (non-designer-mind) ideas.
The wording in the PowerPoint must be included. You are free to use all my logos and images attached in whichever way you think works best. Feel free to use other yoga/scenic imagery you find which may be suitable.

Please stick to these font options:
Logo font: Amatic
Main text font: Raleway

Colour palette in the branding guidelines attached.

Font styles to use
Other font styles liked:
• Amatic + Raleway

Requirements
Must have
• Colour palette as per attached branding guidelines
• Fonts Amatic + Raleway
• Same design style but 2 different layouts for the 2 different promotions
• My logo must be included
• Call to action to book a session
• Wording as per PowerPoint attached
• Contact details - email, phone and website
Nice to have
• Optional other relevant yoga/lavender themed imagery
• Picture of me (to build familiarity with customers)

```html
<!DOCTYPE html>
<html lang="en">
<head>
<meta charset="utf-8">
<title>Cobaltine Pilates – Summer Flyers</title>
<link rel="stylesheet" href="https://fonts.googleapis.com/css2?family=Amatic+SC:wght@400;700&family=Raleway:wght@400;500;600&display=swap">
<style>
  :root{
    --stage:#5b5b5e;
    --paper:#ffffff;
    --plum:#9a80a6;
    --plum-dark:#8a6f97;
    --plum-soft:#b8a5c2;
    --plum-text:#9176a0;
    --ink:#4b4b4b;
    --rose:#f2b3c2;
    --rose-deep:#e98fa6;
    --cta:#b07d9c;
  }
  *{box-sizing:border-box;margin:0;padding:0}
  html,body{width:1200px;height:874px;overflow:hidden;background:var(--stage)}
  body{position:relative;font-family:'Raleway',sans-serif;color:var(--ink)}

  .flyer{position:absolute;top:53px;width:545px;height:768px;background:var(--paper);overflow:hidden;box-shadow:0 4px 14px rgba(0,0,0,.35)}
  .flyer--friend{left:38px}
  .flyer--package{left:618px}

  .abs{position:absolute}

  .hero{position:absolute;left:0;top:0;width:545px}
  .flyer--friend .hero{height:380px;background:linear-gradient(180deg,#f4f1ef 0%,#ece6e3 40%,#e4dad6 70%,rgba(255,255,255,0) 100%)}
  .flyer--package .hero{height:330px;background:linear-gradient(160deg,#2f3b63 0%,#4f6e86 30%,#8bb3ad 55%,#c9dccf 75%,rgba(255,255,255,0) 100%)}

  .brand{position:absolute;font-family:'Amatic SC',sans-serif;font-weight:400;font-size:34px;letter-spacing:1px;line-height:1}
  .flyer--friend .brand{left:26px;top:92px;color:#6f6f73}
  .flyer--package .brand{left:28px;top:82px;color:#ffffff}
  .brand-dot{position:absolute;width:12px;height:12px;border-radius:50%}
  .flyer--friend .brand-dot{left:84px;top:68px;background:var(--plum)}
  .flyer--package .brand-dot{left:86px;top:58px;background:#ffffff}

  .title-band{position:absolute;background:var(--plum);opacity:.92;color:#fff;font-family:'Amatic SC',sans-serif;font-weight:400;line-height:1;display:flex;align-items:center}
  .flyer--friend .title-band{left:0;top:300px;width:338px;height:66px;font-size:44px;padding-left:28px;clip-path:polygon(0 8%,96% 0,100% 40%,97% 100%,0 92%)}
  .flyer--package .title-band{left:114px;top:170px;width:308px;height:44px;font-size:38px;padding-left:32px;clip-path:polygon(2% 10%,98% 0,100% 60%,96% 100%,0 88%)}

  .badge{position:absolute;left:366px;top:237px;width:124px;height:124px;border-radius:50%;background:var(--plum);border:3px solid rgba(255,255,255,.7);color:#fff;font-family:'Amatic SC',sans-serif;text-align:center;display:flex;flex-direction:column;justify-content:center;line-height:1}
  .badge__small{font-size:18px}
  .badge__big{font-size:40px;font-weight:700;margin:2px 0}

  .body-copy{position:absolute;font-size:12.2px;line-height:18.4px;color:var(--ink)}
  .body-copy p+p{margin-top:18px}
  .flyer--friend .body-copy{left:29px;top:381px;width:310px}
  .flyer--package .intro{left:0;top:253px;width:545px;text-align:center;font-size:14px;line-height:20px}
  .flyer--package .intro p+p{margin-top:20px}

  .subhead{position:absolute;left:0;top:222px;width:545px;text-align:center;color:var(--plum-text);font-weight:600;font-size:21px}

  .tag{position:absolute;height:26px;background:var(--plum);color:#fff;font-weight:600;font-size:13px;line-height:26px;padding-left:6px;clip-path:polygon(0 0,100% 0,94% 50%,100% 100%,0 100%)}
  .tag-text{position:absolute;font-size:12.5px;line-height:16.5px;color:var(--ink)}

  .price-bar{position:absolute;left:29px;width:224px;height:26px;color:#fff;font-size:14px;line-height:26px;padding-left:7px;clip-path:polygon(0 0,96% 0,100% 50%,96% 100%,0 100%)}
  .price-bar--dark{background:var(--plum-dark)}
  .price-bar--light{background:var(--plum-soft)}

  .portrait{position:absolute;left:410px;top:400px;width:135px;height:300px;background:linear-gradient(90deg,rgba(255,255,255,0) 0%,rgba(230,220,228,.7) 45%,rgba(220,205,215,.8) 100%)}

  .packages{position:absolute;left:0;top:492px;width:545px;height:80px}
  .package{position:absolute;top:0;width:164px;text-align:center;color:var(--ink)}
  .package__label{font-size:13px}
  .package__price{font-size:29px;font-weight:600;color:var(--plum-text);line-height:34px;margin-top:2px}
  .package__save{font-size:13.5px}
  .package-rule{position:absolute;top:-4px;width:1.5px;height:76px;background:var(--plum)}

  .lotus{position:absolute;background:radial-gradient(ellipse at 70% 80%,var(--rose-deep) 0%,var(--rose) 45%,rgba(255,255,255,0) 75%)}
  .flyer--friend .lotus{left:302px;top:507px;width:243px;height:212px}
  .flyer--package .lotus{left:338px;top:590px;width:207px;height:133px}

  .cta{position:absolute;font-family:'Amatic SC',sans-serif;font-weight:400;color:var(--cta);text-align:center;line-height:1}
  .flyer--friend .cta{left:340px;top:642px;width:180px;font-size:32px}
  .flyer--package .cta{left:364px;top:648px;width:172px;font-size:31px}

  .footer{position:absolute;left:0;bottom:0;width:545px;height:48px;background:var(--plum);color:#fff;display:flex;align-items:center}
  .contact{position:absolute;display:flex;align-items:center;gap:6px;white-space:nowrap}
  .contact svg{width:14px;height:14px;fill:none;stroke:#fff;stroke-width:1.8}
  .contact--phone{left:30px;font-weight:600;font-size:16px}
  .contact--web{left:206px;font-size:12.5px}
  .contact--mail{left:373px;font-size:11.5px}
</style>
</head>
<body>

<!-- Flyer one: bring a friend -->
<section class="flyer flyer--friend">
  <div class="hero" role="img" aria-label="Photo of the instructor smiling in a seated yoga stretch in a bright room"></div>
  <span class="brand-dot"></span>
  <div class="brand">Cobaltine Pilates</div>

  <div class="title-band">Private Yoga Classes</div>

  <div class="badge">
    <span class="badge__small">Bring a friend for</span>
    <span class="badge__big">FREE</span>
    <span class="badge__small">this summer!</span>
  </div>

  <div class="body-copy">
    <p>Going to a new yoga class can be a little intimidating.<br>Where do I put my mat? Does it matter I can't even<br>touch my toes? What language will they speak? I get<br>it. I've been there.</p>
    <p>So instead, how about trying private yoga classes?<br>We can practice at the best time for your schedule.<br>And make it even more fun by doing it with your<br>friend.</p>
    <p>This summer if you book a private class with me you<br>can now do just that, and bring a friend along for free!</p>
  </div>

  <div class="tag" style="left:360px;top:384px;width:149px">Offer period</div>
  <div class="tag-text" style="left:365px;top:416px">July to September 2017</div>
  <div class="tag" style="left:360px;top:450px;width:149px">Location</div>
  <div class="tag-text" style="left:365px;top:484px;width:140px">Let's discuss! I have options to use studio spaces or we can do it at yours' or your friend's home</div>

  <div class="price-bar price-bar--dark" style="top:612px">60 minutes – 120fr (60fr each!)</div>
  <div class="price-bar price-bar--light" style="top:642px">75 minutes – 150fr (75fr each!)</div>
  <div class="price-bar price-bar--dark" style="top:671px">90 minutes – 180fr (90fr each!)</div>

  <div class="lotus" role="img" aria-label="Pink lotus petal illustration"></div>
  <div class="cta">Get in touch to<br>book your session!</div>

  <footer class="footer">
    <div class="contact contact--phone"><svg viewBox="0 0 24 24"><path d="M5 3h4l2 5-3 2a11 11 0 0 0 6 6l2-3 5 2v4a2 2 0 0 1-2 2A17 17 0 0 1 3 5a2 2 0 0 1 2-2z"/></svg>0712 555 308</div>
    <div class="contact contact--web"><svg viewBox="0 0 24 24"><circle cx="12" cy="12" r="9"/><path d="M3 12h18M12 3c3 3 3 15 0 18M12 3c-3 3-3 15 0 18"/></svg>www.cobaltine.fit</div>
    <div class="contact contact--mail"><svg viewBox="0 0 24 24"><rect x="3" y="5" width="18" height="14"/><path d="M3 6l9 7 9-7"/></svg>hello@cobaltine.fit</div>
  </footer>
</section>

<!-- Flyer two: 4 for 3 package -->
<section class="flyer flyer--package">
  <div class="hero" role="img" aria-label="Scenic photo of a person in tree pose on a cliff above a fjord"></div>
  <span class="brand-dot"></span>
  <div class="brand">Cobaltine Pilates</div>

  <div class="title-band">Private Yoga Classes</div>
  <div class="subhead">4 classes for the price of 3</div>

  <div class="portrait" role="img" aria-label="Faded photo of the instructor with hands in prayer position"></div>

  <div class="body-copy intro">
    <p>Would you like to develop a home yoga practice? Do you<br>have a particular yoga pose or series of poses you'd like to<br>work on? Or perhaps you'd just like an opportunity to ask<br>questions and dive deeper into your yoga practice?</p>
    <p>Private classes are the perfect way to do this! And this<br>summer Cobaltine Pilates is offering a private class package to<br>help you really make the most of your yoga practice.</p>
    <p>During July to September 2017, if you book 3 private yoga<br>classes you will get the 4th for free!</p>
  </div>

  <div class="packages">
    <div class="package" style="left:27px">
      <div class="package__label">60 minute package</div>
      <div class="package__price">360fr</div>
      <div class="package__save">(save 120fr)</div>
    </div>
    <span class="package-rule" style="left:190px"></span>
    <div class="package" style="left:190px">
      <div class="package__label">75 minute package</div>
      <div class="package__price">450fr</div>
      <div class="package__save">(save 150fr)</div>
    </div>
    <span class="package-rule" style="left:354px"></span>
    <div class="package" style="left:353px">
      <div class="package__label">90 minute package</div>
      <div class="package__price">540fr</div>
      <div class="package__save">(save 180fr)</div>
    </div>
  </div>

  <div class="tag" style="left:16px;top:586px;width:147px">Offer period</div>
  <div class="tag-text" style="left:21px;top:617px">July to September 2017</div>
  <div class="tag" style="left:16px;top:648px;width:147px">Location</div>
  <div class="tag-text" style="left:21px;top:681px;width:300px">Let's discuss! I have options to use studio spaces<br>or we can do it at yours' or your friend's home</div>

  <div class="lotus" role="img" aria-label="Pink lotus petal illustration"></div>
  <div class="cta">Get in touch to<br>book your session!</div>

  <footer class="footer">
    <div class="contact contact--phone"><svg viewBox="0 0 24 24"><path d="M5 3h4l2 5-3 2a11 11 0 0 0 6 6l2-3 5 2v4a2 2 0 0 1-2 2A17 17 0 0 1 3 5a2 2 0 0 1 2-2z"/></svg>0712 555 308</div>
    <div class="contact contact--web"><svg viewBox="0 0 24 24"><circle cx="12" cy="12" r="9"/><path d="M3 12h18M12 3c3 3 3 15 0 18M12 3c-3 3-3 15 0 18"/></svg>www.cobaltine.fit</div>
    <div class="contact contact--mail"><svg viewBox="0 0 24 24"><rect x="3" y="5" width="18" height="14"/><path d="M3 6l9 7 9-7"/></svg>hello@cobaltine.fit</div>
  </footer>
</section>

</body>
</html>
```